Fun and Splashy Flyer Design

We need a flyer designed for our new car cleaning brand! We have looked around, and the stock options either look way too dark/serious/exclusive, or they look too shiny/stock image.

We need something that can be more subtle, that works with our work van.

For this project we would like a photoshop file with individual layers, and you can just put placeholder text for the main slogan, a header 1, header 2, bullet point and body text.

What we're really looking for are the transitions between images and elements, font colours and pairings and design accents.

We want the brand to be fun, clean, happy and straightforward (slightly minimalist). Please message if you have any questions!

```html
<!DOCTYPE html>
<html lang="en">
<head>
<meta charset="utf-8">
<title>Bright Bay Car Care – Flyer</title>
<link rel="stylesheet" href="https://fonts.googleapis.com/css2?family=Barlow:wght@400;500;600;700;800;900&display=swap">
<style>
  :root{
    --blue:#1a5c94;
    --blue-dark:#164a7a;
    --blue-bright:#1c8fd6;
    --yellow:#f8d816;
    --yellow-warm:#fbc82a;
    --tag:#fcbf19;
    --price:#ffe21a;
    --white:#ffffff;
    --ink:#163f6b;
  }
  *{margin:0;padding:0;box-sizing:border-box;}
  html,body{width:900px;height:1200px;overflow:hidden;background:#e9e9ea;}
  body{font-family:"Barlow",Arial,sans-serif;}
  .flyer{position:relative;width:900px;height:1200px;overflow:hidden;background:linear-gradient(160deg,var(--yellow) 40%,var(--yellow-warm) 100%);}
  .backdrop{position:absolute;inset:0;}

  .brand-ribbon{position:absolute;left:634px;top:0;width:197px;height:150px;background:linear-gradient(180deg,var(--blue-bright),var(--blue));}
  .brand-badge{position:absolute;left:636px;top:36px;width:192px;height:192px;border-radius:50%;background:var(--blue);display:flex;align-items:center;justify-content:center;box-shadow:0 4px 10px rgba(0,0,0,.25);}
  .brand-badge__inner{width:162px;height:162px;border-radius:50%;background:var(--yellow);display:flex;align-items:center;justify-content:center;text-align:center;}
  .brand-name{font-weight:800;font-size:22px;line-height:1.05;color:var(--blue-dark);text-transform:uppercase;}

  .price-list{position:absolute;left:45px;width:379px;height:357px;border:5px solid var(--white);border-radius:14px;background:linear-gradient(135deg,var(--blue-bright) 0%,var(--blue) 70%);}
  .price-list--first{top:400px;}
  .price-list--second{top:800px;}
  .price-list__title{position:absolute;left:50%;top:-12px;transform:translateX(-50%);width:176px;height:44px;background:var(--blue-dark);border-radius:0 0 12px 12px;color:var(--white);font-weight:500;font-size:18px;letter-spacing:.3px;display:flex;align-items:center;justify-content:center;}
  .price-list__title::before{content:"";position:absolute;top:0;left:-12px;right:-12px;height:12px;background:var(--blue-dark);clip-path:polygon(12px 0,calc(100% - 12px) 0,100% 100%,0 100%);}
  .price-row{position:absolute;left:-16px;width:370px;height:40px;display:flex;align-items:center;}
  .price-row__tag{width:138px;height:40px;background:var(--tag);clip-path:polygon(0 0,94% 0,100% 50%,94% 100%,0 100%);color:var(--ink);font-size:16px;font-weight:500;padding-left:17px;display:flex;align-items:center;}
  .price-row__desc{width:150px;margin-left:10px;color:var(--white);font-size:12px;line-height:1.1;}
  .price-row__price{margin-left:6px;color:var(--price);font-size:23px;font-weight:500;}

  .feature{position:absolute;left:460px;width:400px;height:98px;display:flex;}
  .feature__num{width:100px;height:98px;border-radius:6px;background:linear-gradient(135deg,var(--blue-bright),var(--blue-dark));color:var(--white);font-weight:900;font-size:58px;display:flex;align-items:center;justify-content:center;box-shadow:0 3px 6px rgba(0,0,0,.2);}
  .feature__text{margin-left:20px;padding-top:6px;color:var(--ink);}
  .feature__title{font-weight:700;font-size:21px;color:var(--blue-bright);line-height:1.1;}
  .feature:nth-of-type(n) .feature__title{color:var(--blue);}
  .feature--one .feature__title{color:var(--blue-bright);}
  .feature__body{font-size:14.5px;line-height:1.3;color:var(--blue);letter-spacing:.2px;}

  .contact-band-edge{position:absolute;left:0;top:987px;width:48px;height:120px;background:var(--blue);}
  .contact{position:absolute;left:424px;top:987px;width:422px;height:120px;background:var(--blue);border-radius:0 10px 10px 0;color:var(--white);padding:12px 0 0 22px;}
  .contact__phone{font-weight:700;font-size:38px;line-height:1.1;}
  .contact__web{font-weight:700;font-size:29px;line-height:1.3;}

  .social{position:absolute;left:700px;top:1126px;display:flex;align-items:center;gap:8px;color:var(--blue-dark);font-weight:600;font-size:15px;}
  .social__square{width:26px;height:26px;background:var(--blue);border-radius:3px;}
</style>
</head>
<body>
<main class="flyer">
  <svg class="backdrop" width="900" height="1200" viewBox="0 0 900 1200">
    <defs>
      <linearGradient id="photoTone" x1="0" y1="0" x2="1" y2="1">
        <stop offset="0" stop-color="#9fb7c9"/>
        <stop offset="0.4" stop-color="#e4e6e6"/>
        <stop offset="0.75" stop-color="#cfd3d6"/>
        <stop offset="1" stop-color="#7f8a92"/>
      </linearGradient>
    </defs>
    <path role="img" aria-label="Photo of a worker pressure-washing a car covered in white foam"
          d="M0 0 H900 V453 C760 540 560 612 420 622 L0 618 Z" fill="url(#photoTone)"/>
    <path d="M0 0 H212 Q60 60 0 180 Z" fill="#1a5c94"/>
    <path d="M320 0 H430 Q300 20 230 60 Q270 20 320 0 Z" fill="#f2e9b4" opacity=".6"/>
    <circle cx="180" cy="165" r="18" fill="none" stroke="#fff" stroke-width="2" stroke-dasharray="5 4"/>
    <path d="M172 182 Q120 230 105 300" fill="none" stroke="#fff" stroke-width="2" stroke-dasharray="6 5"/>
    <path d="M424 582 C600 530 780 430 900 330" fill="none" stroke="#1a5c94" stroke-width="2" stroke-dasharray="7 5"/>
    <circle cx="890" cy="680" r="34" fill="none" stroke="#b89a3a" stroke-width="2" stroke-dasharray="6 5" transform="translate(-2 0)"/>
    <path d="M895 715 Q920 780 1010 840" fill="none" stroke="#b89a3a" stroke-width="2" stroke-dasharray="6 5" transform="translate(-100 0)"/>
    <path d="M900 945 Q800 980 765 1070 Q730 1140 742 1200" fill="none" stroke="#b89a3a" stroke-width="2" stroke-dasharray="6 5"/>
    <circle cx="830" cy="880" r="23" fill="#1a5c94"/>
  </svg>

  <div class="brand-ribbon"></div>
  <div class="brand-badge">
    <div class="brand-badge__inner"><span class="brand-name">Bright Bay<br>Car Care</span></div>
  </div>

  <section class="price-list price-list--first">
    <h2 class="price-list__title">LOREM IPSUM</h2>
    <div class="price-row" style="top:57px"><span class="price-row__tag">Lorem ipsum</span><span class="price-row__desc">Lorem ipsum dolor sit amet, consectetuer adipiscing elit, sed</span><span class="price-row__price">$00.00</span></div>
    <div class="price-row" style="top:113px"><span class="price-row__tag">Lorem ipsum</span><span class="price-row__desc">Lorem ipsum dolor sit amet, consectetuer adipiscing elit, sed</span><span class="price-row__price">$00.00</span></div>
    <div class="price-row" style="top:170px"><span class="price-row__tag">Lorem ipsum</span><span class="price-row__desc">Lorem ipsum dolor sit amet, consectetuer adipiscing elit, sed</span><span class="price-row__price">$00.00</span></div>
    <div class="price-row" style="top:226px"><span class="price-row__tag">Lorem ipsum</span><span class="price-row__desc">Lorem ipsum dolor sit amet, consectetuer adipiscing elit, sed</span><span class="price-row__price">$00.00</span></div>
    <div class="price-row" style="top:282px"><span class="price-row__tag">Lorem ipsum</span><span class="price-row__desc">Lorem ipsum dolor sit amet, consectetuer adipiscing elit, sed</span><span class="price-row__price">$00.00</span></div>
  </section>

  <div class="contact-band-edge"></div>

  <section class="price-list price-list--second">
    <h2 class="price-list__title">LOREM IPSUM</h2>
    <div class="price-row" style="top:57px"><span class="price-row__tag">Lorem ipsum</span><span class="price-row__desc">Lorem ipsum dolor sit amet, consectetuer adipiscing elit, sed</span><span class="price-row__price">$00.00</span></div>
    <div class="price-row" style="top:113px"><span class="price-row__tag">Lorem ipsum</span><span class="price-row__desc">Lorem ipsum dolor sit amet, consectetuer adipiscing elit, sed</span><span class="price-row__price">$00.00</span></div>
    <div class="price-row" style="top:170px"><span class="price-row__tag">Lorem ipsum</span><span class="price-row__desc">Lorem ipsum dolor sit amet, consectetuer adipiscing elit, sed</span><span class="price-row__price">$00.00</span></div>
    <div class="price-row" style="top:226px"><span class="price-row__tag">Lorem ipsum</span><span class="price-row__desc">Lorem ipsum dolor sit amet, consectetuer adipiscing elit, sed</span><span class="price-row__price">$00.00</span></div>
    <div class="price-row" style="top:282px"><span class="price-row__tag">Lorem ipsum</span><span class="price-row__desc">Lorem ipsum dolor sit amet, consectetuer adipiscing elit, sed</span><span class="price-row__price">$00.00</span></div>
  </section>

  <article class="feature feature--one" style="top:637px">
    <div class="feature__num">01</div>
    <div class="feature__text"><h3 class="feature__title">LOREM IPSUM</h3><p class="feature__body">Lorem ipsum dolor sit amet,<br>consectetuer adipiscing elitdiam<br>consectetuer.</p></div>
  </article>
  <article class="feature" style="top:752px">
    <div class="feature__num">02</div>
    <div class="feature__text"><h3 class="feature__title">LOREM IPSUM</h3><p class="feature__body">Lorem ipsum dolor sit amet,<br>consectetuer adipiscing elitdiam<br>consectetuer.</p></div>
  </article>
  <article class="feature" style="top:868px">
    <div class="feature__num">03</div>
    <div class="feature__text"><h3 class="feature__title">LOREM IPSUM</h3><p class="feature__body">Lorem ipsum dolor sit amet,<br>consectetuer adipiscing elitdiam<br>consectetuer.</p></div>
  </article>

  <section class="contact">
    <p class="contact__phone">(+505) 555 018 240</p>
    <p class="contact__web">www.brightbaycare.ca</p>
  </section>

  <div class="social"><span class="social__square"></span><span>@brightbaycare</span></div>
</main>
</body>
</html>
```